Tolliver Business Services Stationary
Letterhead, Business Card, Envelope
Tolliver Business Services Stationary -
Creative Brief
Simple
Dale Pruett
Bookkeeping and Tax Preparation
PO Box 4713 Seattle, WA 98109
dpruettpruett@tolliverllc.example
www.tolliverllc.example
The info for the business card is fake because this is not a private contest. I will provide the correct info when I finalize the contest. I need a standard sized business card, letterhead, and envelope. Finished artwork needs to be vector format. I have attached designs that I like and my company logo.
Maybe just the logo? reversed colors? I've attached samples and layouts the I like.

```html
<!DOCTYPE html>
<html lang="en">
<head>
<meta charset="utf-8">
<title>Tolliver Business Services Stationery</title>
<link href="https://fonts.googleapis.com/css2?family=Cormorant+Garamond:wght@500&family=Crimson+Text:wght@400&display=swap" rel="stylesheet">
<style>
  :root {
    --backdrop: #c9c9c9;
    --paper: #ffffff;
    --ink: #1a1a1a;
    --ink-soft: #6b6b6b;
    --card-dark: #0d0d0d;
    --card-dark-text: #d8d8d8;
    --flap: #5a5a5a;
    --flap-text: #e6e6e6;
    --shadow: 0 2px 6px rgba(0,0,0,0.18);
  }
  * { margin: 0; padding: 0; box-sizing: border-box; }
  html, body { width: 1200px; height: 1104px; overflow: hidden; }
  body {
    background: var(--backdrop);
    position: relative;
    font-family: "Crimson Text", Georgia, serif;
    color: var(--ink);
  }
  .sheet { position: absolute; background: var(--paper); box-shadow: var(--shadow); }

  /* Wordmark */
  .wordmark { position: absolute; display: flex; align-items: center; gap: 12px; }
  .wordmark__square { width: 22px; height: 22px; background: var(--ink); flex: none; }
  .wordmark__name {
    font-family: "Cormorant Garamond", Georgia, serif;
    font-weight: 500; text-transform: uppercase; letter-spacing: 2px;
    color: var(--ink); line-height: 1;
  }

  /* Letterhead */
  .letterhead { left: 186px; top: 42px; width: 669px; height: 864px; }
  .letterhead .wordmark { left: 36px; top: 40px; }
  .letterhead .wordmark__name { font-size: 38px; }
  .letterhead__footer {
    position: absolute; left: 90px; bottom: 24px;
    font-size: 11px; line-height: 14px; color: var(--ink-soft);
  }

  /* Business card, front */
  .card-front { left: 42px; top: 147px; width: 279px; height: 165px; }
  .card-front__line {
    position: absolute; left: 12px; top: 12px; right: 12px;
    font-size: 8px; color: var(--ink-soft); white-space: nowrap;
  }
  .card-front .wordmark { left: 120px; top: 66px; gap: 7px; }
  .card-front .wordmark__square { width: 12px; height: 12px; }
  .card-front .wordmark__name { font-size: 18px; letter-spacing: 1px; }

  /* Business card, back */
  .card-back { left: 42px; top: 354px; width: 279px; height: 162px; background: var(--card-dark); }
  .card-back__contact {
    position: absolute; left: 180px; top: 24px;
    font-size: 8.5px; line-height: 11px; color: var(--card-dark-text);
  }
  .card-back__web {
    position: absolute; left: 180px; bottom: 20px;
    font-size: 8.5px; color: var(--card-dark-text);
  }

  /* Envelope, back */
  .envelope-back { left: 408px; top: 390px; width: 753px; height: 333px; }
  .envelope-back__flap { position: absolute; left: 0; top: 0; }
  .envelope-back__mark {
    position: absolute; left: 50%; top: 34px; transform: translateX(-50%);
    width: 18px; height: 18px; background: var(--flap-text);
  }
  .envelope-back__web {
    position: absolute; left: 0; right: 0; top: 66px; text-align: center;
    font-size: 10px; color: var(--flap-text); letter-spacing: 0.5px;
  }

  /* Envelope, front */
  .envelope-front { left: 408px; top: 744px; width: 753px; height: 324px; }
  .envelope-front .wordmark { left: 36px; top: 42px; }
  .envelope-front .wordmark__name { font-size: 34px; }
  .envelope-front__return {
    position: absolute; left: 72px; top: 88px;
    font-size: 10px; color: var(--ink-soft);
  }
</style>
</head>
<body>

  <section class="sheet letterhead" aria-label="Letterhead">
    <div class="wordmark">
      <span class="wordmark__square"></span>
      <span class="wordmark__name">Tolliver</span>
    </div>
    <address class="letterhead__footer">
      PO Box 4713<br>
      Seattle, WA 98109<br>
      Phone 206.555.0148<br>
      Fax 206.555.0149<br>
      www.tolliverllc.example
    </address>
  </section>

  <section class="sheet card-front" aria-label="Business card front">
    <p class="card-front__line">Dale Pruett &nbsp;|&nbsp; Bookkeeping and Tax Preparation</p>
    <div class="wordmark">
      <span class="wordmark__square"></span>
      <span class="wordmark__name">Tolliver</span>
    </div>
  </section>

  <section class="sheet card-back" aria-label="Business card back">
    <address class="card-back__contact">
      PO Box 4713<br>
      Seattle, WA 98109<br>
      Phone 206.555.0148<br>
      Fax 206.555.0149
    </address>
    <p class="card-back__web">www.tolliverllc.example</p>
  </section>

  <section class="sheet envelope-back" aria-label="Envelope back">
    <svg class="envelope-back__flap" width="753" height="110" viewBox="0 0 753 110" aria-hidden="true">
      <polygon points="0,0 753,0 753,76 720,104 33,104 0,76" fill="var(--flap)"/>
    </svg>
    <span class="envelope-back__mark"></span>
    <p class="envelope-back__web">www.tolliverllc.example</p>
  </section>

  <section class="sheet envelope-front" aria-label="Envelope front">
    <div class="wordmark">
      <span class="wordmark__square"></span>
      <span class="wordmark__name">Tolliver</span>
    </div>
    <p class="envelope-front__return">PO Box 4713 Seattle, WA 98109</p>
  </section>

</body>
</html>
```